Attract renters to our neighborhoods - inform renters who we are

Apartments in several neighborhoods. We want to attract renters who want to live along the lake or other near by neighborhoods. We want them to know that we have an apartment for them in their location.
The perfect location to spend your time.
When minutes matter LIVE where you work and play! (love this tag line)
Updates

www.kvtresidences.example Choose from over 3,700 apartments in Chicago’s most celebrated neighborhoods. 773-582-6041 Chicago’s most celebrated neighborhoods. 31 PROPERTIES

Target Market(s)

Sophisticated apartment renter who wants location, space, amenities

Industry/Entity Type

Apartment Rentals

Requirements
Must have
• Feel like I want to live there, or the ad is calling me
Nice to have
• Appeal to a sophisticated apartment renter. We have what you want, where you want to be.
Should not have
• Logo colors are black and red/burnt orange see attached logo

```html
<!DOCTYPE html>
<html lang="en">
<head>
<meta charset="utf-8">
<title>KVT Residences Flyer</title>
<link href="https://fonts.googleapis.com/css2?family=Ubuntu:wght@400;500;700&family=Kaushan+Script&display=swap" rel="stylesheet">
<style>
  :root {
    --red: #c0312b;
    --red-dark: #a8241f;
    --black: #111111;
    --ink: #1c1c1c;
    --paper: #ffffff;
    --backdrop: #e9e7e4;
    --room-light: #e4e2de;
    --room-mid: #b9b8b4;
    --sky: #5b9fd0;
    --lake: #2fa7b8;
    --city: #8d8f8e;
  }
  html, body {
    margin: 0;
    padding: 0;
    width: 1200px;
    height: 771px;
    overflow: hidden;
    background: var(--backdrop);
  }
  .canvas {
    position: relative;
    width: 1200px;
    height: 771px;
  }
  .flyer {
    position: absolute;
    left: 320px;
    top: 22px;
    width: 611px;
    height: 793px;
    background: var(--paper);
    transform: scale(0.917);
    transform-origin: top left;
    overflow: hidden;
    font-family: "Ubuntu", sans-serif;
    color: var(--ink);
  }
  .hero-shapes {
    position: absolute;
    left: 0;
    top: 0;
    width: 611px;
    height: 793px;
  }
  .tagline-badge {
    position: absolute;
    left: 417px;
    top: 325px;
    width: 164px;
    height: 164px;
    border-radius: 50%;
    background: var(--black);
    box-shadow: 0 0 0 2px var(--paper), 0 0 0 3px var(--black);
    color: var(--paper);
    font-family: "Kaushan Script", cursive;
    font-size: 19px;
    line-height: 25px;
    text-align: center;
    display: flex;
    align-items: center;
    justify-content: center;
  }
  .brand {
    position: absolute;
    left: 29px;
    top: 462px;
    display: flex;
    align-items: center;
    gap: 10px;
    font-weight: 700;
    font-size: 34px;
    color: var(--black);
    letter-spacing: 0.5px;
  }
  .brand-mark {
    width: 22px;
    height: 22px;
    background: var(--red);
  }
  .headline {
    position: absolute;
    left: 25px;
    top: 543px;
    margin: 0;
    font-weight: 500;
    font-size: 20.5px;
    line-height: 26px;
    text-transform: uppercase;
    color: var(--black);
  }
  .headline .accent {
    color: var(--red);
    font-weight: 700;
  }
  .intro {
    position: absolute;
    right: 25px;
    top: 538px;
    margin: 0;
    width: 210px;
    text-align: right;
    font-size: 13px;
    line-height: 17px;
    color: #333;
  }
  .neighborhoods {
    position: absolute;
    left: 28px;
    top: 605px;
    width: 561px;
    display: flex;
    gap: 8.5px;
    margin: 0;
    padding: 0;
    list-style: none;
  }
  .neighborhood {
    width: 134px;
    height: 105px;
    position: relative;
  }
  .neighborhood-photo {
    position: absolute;
    inset: 0 0 14px 0;
    background: linear-gradient(180deg, var(--sky) 0%, #9cc7e4 30%, var(--city) 55%, var(--lake) 100%);
  }
  .neighborhood-name {
    position: absolute;
    left: 0; right: 0; bottom: 0;
    height: 14px;
    background: var(--red);
    color: var(--paper);
    font-size: 7px;
    font-weight: 700;
    line-height: 14px;
    text-align: center;
    text-transform: uppercase;
    letter-spacing: -0.2px;
  }
  .caption {
    position: absolute;
    left: 0; right: 0;
    top: 721px;
    margin: 0;
    text-align: center;
    font-size: 14px;
    color: var(--black);
  }
  .caption .count { color: var(--red); }
  .footer-web, .footer-tour {
    position: absolute;
    top: 765px;
    font-size: 15px;
    color: var(--paper);
    display: flex;
    align-items: center;
    gap: 8px;
  }
  .footer-web { left: 32px; font-weight: 500; }
  .footer-tour { left: 340px; font-weight: 700; font-size: 14px; }
  .footer-tour .phone { display: flex; align-items: center; gap: 4px; margin-left: 6px; }
</style>
</head>
<body>
<div class="canvas">
  <article class="flyer">
    <svg class="hero-shapes" viewBox="0 0 611 793" aria-hidden="false">
      <defs>
        <linearGradient id="roomTone" x1="0" y1="0" x2="1" y2="1">
          <stop offset="0" stop-color="#d9d7d2"/>
          <stop offset="0.5" stop-color="var(--room-light)"/>
          <stop offset="1" stop-color="var(--room-mid)"/>
        </linearGradient>
      </defs>
      <polygon role="img" aria-label="Photo of a bright apartment living room with grey sofa, dining table and city-view windows"
               points="0,0 611,0 611,285 286,495 0,310" fill="url(#roomTone)"/>
      <polygon class="shade-dark" points="0,0 150,0 306,205 0,285" fill="#1a1a1a" opacity="0.78"/>
      <polygon class="shade-red" points="0,0 611,0 306,205" fill="var(--red)" opacity="0.93"/>
      <polygon class="shade-red-soft" points="420,0 611,0 611,40" fill="var(--red-dark)" opacity="0.6"/>
      <polygon class="band-dark" points="0,752 300,752 318,793 0,793" fill="var(--black)"/>
      <polygon class="band-red" points="300,752 611,752 611,793 318,793" fill="var(--red)"/>
    </svg>

    <div class="tagline-badge"><span>The perfect<br>location to spend<br>your time.</span></div>

    <div class="brand"><span class="brand-mark"></span><span>KVT Residences</span></div>

    <h1 class="headline">When minutes matter <span class="accent">Live</span><br>where you work and play</h1>

    <p class="intro">Choose from over<br>3,700 apartments in Chicago’s<br>most celebrated neighborhoods.</p>

    <ul class="neighborhoods">
      <li class="neighborhood"><div class="neighborhood-photo" role="img" aria-label="Aerial view of Gold Coast and Old Town skyline by the lake"></div><span class="neighborhood-name">Gold Coast &amp; Old Town</span></li>
      <li class="neighborhood"><div class="neighborhood-photo" role="img" aria-label="Aerial view of River North towers"></div><span class="neighborhood-name">River North</span></li>
      <li class="neighborhood"><div class="neighborhood-photo" role="img" aria-label="Aerial view of Lincoln Park beach and lakefront"></div><span class="neighborhood-name">Lincoln Park</span></li>
      <li class="neighborhood"><div class="neighborhood-photo" role="img" aria-label="Aerial view of Lakeview harbor and shoreline"></div><span class="neighborhood-name">Lakeview</span></li>
    </ul>

    <p class="caption">Chicago’s most celebrated neighborhoods. <span class="count">31 Properties</span></p>

    <div class="footer-web">
      <svg width="12" height="12" viewBox="0 0 12 12" aria-hidden="true"><circle cx="6" cy="6" r="5" fill="none" stroke="#fff" stroke-width="1.2"/><ellipse cx="6" cy="6" rx="2.2" ry="5" fill="none" stroke="#fff" stroke-width="1"/><line x1="1" y1="6" x2="11" y2="6" stroke="#fff" stroke-width="1"/></svg>
      <span>www.kvtresidences.example</span>
    </div>
    <div class="footer-tour">
      <span>SHEDULE A TOUR</span>
      <span class="phone">
        <svg width="13" height="13" viewBox="0 0 14 14" aria-hidden="true"><circle cx="7" cy="7" r="6" fill="none" stroke="#fff" stroke-width="1.2"/><path d="M4.8 4.2c.4-.3.8-.2 1 .2l.5 1c.1.3 0 .5-.2.7l-.3.3c.4.8 1 1.4 1.8 1.8l.3-.3c.2-.2.4-.3.7-.2l1 .5c.4.2.5.6.2 1-.5.7-1.2.9-2 .5C6.2 9 5 7.8 4.4 6.2c-.3-.8-.2-1.5.4-2z" fill="#fff"/></svg>
        773-582-6041
      </span>
    </div>
  </article>
</div>
</body>
</html>
```